i need a business card for a plumbing company in california

we are a drain cleaning , maintenance plumbing company who is starting new marketing campaign for a tatrench-less pipe installation department .

Target Market(s)

the professional who appreciates time and quality workmanship.

Industry/Entity Type

Plumbing

Colors
0655a3
ec1f27

Requirements
Must have
• the second logo needs to be included
Nice to have
• a focus on the services offered
Should not have
• any underlined words on the brief

```html
<!DOCTYPE html>
<html lang="en">
<head>
<meta charset="utf-8">
<title>Crestflow Plumbing – Business Card</title>
<link rel="stylesheet" href="https://fonts.googleapis.com/css2?family=Arimo:wght@400;700&display=swap">
<style>
  :root {
    --backdrop: #e9e4dc;
    --kraft-light: #dcb68a;
    --kraft-mid: #c9996a;
    --kraft-dark: #c08f60;
    --ink: #111111;
    --rule: #2a2118;
  }
  html, body {
    margin: 0;
    padding: 0;
    width: 1200px;
    height: 900px;
    overflow: hidden;
    background: var(--backdrop);
  }
  .canvas {
    position: relative;
    width: 1200px;
    height: 900px;
    font-family: "Arimo", Arial, sans-serif;
    color: var(--ink);
  }
  .card {
    position: absolute;
    left: 330px;
    width: 556px;
    height: 343px;
    background: radial-gradient(ellipse at 45% 0%, var(--kraft-light) 0%, var(--kraft-mid) 55%, var(--kraft-dark) 100%);
    box-shadow: 0 2px 6px rgba(0,0,0,0.25);
    text-align: center;
  }
  .card--front { top: 90px; }
  .card--back { top: 470px; }

  .contact {
    position: absolute;
    left: 0;
    right: 0;
    top: 80px;
    display: flex;
    flex-direction: column;
    align-items: center;
  }
  .contact__name {
    font-size: 20px;
    font-weight: 700;
    letter-spacing: 0.3px;
    line-height: 24px;
    margin: 0;
  }
  .contact__title {
    font-size: 16px;
    line-height: 20px;
    margin: 0 0 10px;
  }
  .contact__rule {
    width: 195px;
    height: 1px;
    background: var(--rule);
    border: 0;
    margin: 0;
  }
  .contact__list {
    list-style: none;
    padding: 0;
    margin: 10px 0 11px;
    font-size: 16px;
    line-height: 20.5px;
  }
  .contact__label { font-weight: 700; }
  .contact__address {
    font-style: normal;
    font-size: 16px;
    line-height: 20px;
    margin-top: 18px;
  }

  .brand {
    position: absolute;
    left: 0;
    right: 0;
    top: 128px;
    display: flex;
    align-items: center;
    justify-content: center;
    gap: 16px;
  }
  .brand__mark {
    width: 22px;
    height: 22px;
    background: var(--ink);
  }
  .brand__name {
    font-size: 38px;
    font-weight: 700;
    line-height: 40px;
    color: var(--ink);
    text-align: left;
  }
</style>
</head>
<body>
<main class="canvas">
  <section class="card card--front" aria-label="Card front">
    <div class="contact">
      <h1 class="contact__name">DANIEL REYES</h1>
      <p class="contact__title">Managing Director</p>
      <hr class="contact__rule">
      <ul class="contact__list">
        <li><span class="contact__label">P:</span> 044-987 654 321</li>
        <li><span class="contact__label">M:</span> 044-987 654 321</li>
        <li><span class="contact__label">E:</span> info@crestflow.com</li>
        <li><span class="contact__label">W:</span> www.crestflowpipes.com</li>
      </ul>
      <hr class="contact__rule">
      <address class="contact__address">12345, Address Goes Here<br>Country Name, 123456.</address>
    </div>
  </section>

  <section class="card card--back" aria-label="Card back">
    <div class="brand">
      <span class="brand__name">Crestflow<br>Plumbing</span>
      <span class="brand__mark" aria-hidden="true"></span>
    </div>
  </section>
</main>
</body>
</html>
```